Business Card Design Project

Business card incoporating newly designed logo. The business cards will be magnets and I would like the same design as previously provided (Blue colour swatch with logo up the top) Please note that the logo incorporates a website so it needs to be legible.
The blue colours in teh swatch ideally will be in the same range as the blue of the logo.
The copy should all be in the same colour ie. black if in the white lines or white if in the swatch itself
Updates

Hi All

Some of the designs are very close to what I am after.  I have added logo and updated brief to assist with design.  This project is not refundable so I will be selecting a design.

Hi All

We are looking for a business card as per the brief (colour swatch style) as mentioned it is also a magnet so it needs to be created to the specs supplied.  Being a magnet there is also no requirment for reverse design.

Cheers
Marcy

Industry/Entity Type

Business

Requirements
Must have
• Blue colour swatch design. (see attached current example)
KW Coatings logo (colour) up the top
I require 1 design but 2 versions (with two peoples names and mobile numbers)

The magnets will be printed by PrintHollow.com.au And you can find the full specs online http://www.printhollow.com.au/custom-magnets.aspx

```html
<!DOCTYPE html>
<html lang="en">
<head>
<meta charset="utf-8">
<title>KW Coatings – Magnet Business Cards</title>
<link href="https://fonts.googleapis.com/css2?family=Arimo:wght@400;700&display=swap" rel="stylesheet">
<style>
  :root {
    --backdrop: #e4e4e2;
    --card: #ffffff;
    --ink: #1a1a1a;
    --brand-blue: #1f6fa8;
    --brand-orange: #e0562a;
    --swatch-navy: #253481;
    --swatch-royal: #0a4e99;
    --swatch-mid: #3b74b3;
    --swatch-pale: #8fa8c8;
    --font: "Arimo", Arial, sans-serif;
  }
  * { box-sizing: border-box; margin: 0; padding: 0; }
  html, body {
    width: 1200px; height: 547px; overflow: hidden;
    background: var(--backdrop);
    font-family: var(--font);
    color: var(--ink);
  }
  .card-set { position: relative; width: 1200px; height: 547px; }
  .card {
    position: absolute; top: 38px;
    width: 267px; height: 474px;
    background: var(--card);
    box-shadow: 0 2px 6px rgba(0,0,0,.25);
    overflow: hidden;
  }
  .card--plain { left: 31px; }
  .card--striped { left: 321px; }
  .card--kevin { left: 609px; }
  .card--leon { left: 903px; }

  /* logo */
  .brand { display: flex; flex-direction: column; align-items: center; }
  .brand__line { display: flex; align-items: center; gap: 6px; }
  .brand__mark { width: 12px; height: 12px; background: var(--brand-orange); }
  .brand__name {
    font-weight: 700; font-size: 33px; line-height: 1;
    color: var(--brand-blue); letter-spacing: -0.5px;
  }
  .brand__site { font-size: 9px; margin-top: 3px; color: var(--ink); }

  /* front faces */
  .card--plain .brand, .card--striped .brand {
    position: absolute; left: 0; right: 0; top: 180px;
  }
  .front-email {
    position: absolute; left: 0; right: 0; top: 276px;
    text-align: center; font-size: 12.5px;
  }
  .stripe-row { position: absolute; left: 0; width: 267px; height: 60px; display: flex; }
  .stripe-row--top { top: 0; }
  .stripe-row--bottom { bottom: 0; height: 61px; }
  .chip { height: 100%; }
  .chip--pale { width: 28px; background: var(--swatch-pale); }
  .chip--mid { width: 65px; background: var(--swatch-mid); }
  .chip--royal { width: 65px; background: var(--swatch-royal); }
  .chip--navy { width: 28px; background: var(--swatch-navy); }
  .gap { width: 26px; }
  .gap--wide { width: 27px; }
  .gap--end { width: 28px; }

  /* swatch faces */
  .swatch-face { display: flex; flex-direction: column; height: 100%; }
  .swatch-face .brand { height: 81px; justify-content: center; }
  .band { flex: none; height: 68px; }
  .band--navy { background: var(--swatch-navy); }
  .band--royal { background: var(--swatch-royal); height: 65px; }
  .band--mid { background: var(--swatch-mid); }
  .band--pale { background: var(--swatch-pale); }
  .line {
    flex: none; display: flex; align-items: center; justify-content: center;
    text-align: center;
  }
  .line--name { height: 26px; font-size: 16px; }
  .line--phone { height: 27px; font-size: 12.5px; }
  .line--service { height: 24px; font-size: 12.5px; }
  .line--contact { height: 47px; font-size: 12.5px; line-height: 1.25; flex-direction: column; }
</style>
</head>
<body>
<main class="card-set">

  <section class="card card--plain">
    <div class="brand">
      <div class="brand__line"><span class="brand__mark"></span><span class="brand__name">KW Coatings</span></div>
      <span class="brand__site">kwcoatings.com.au</span>
    </div>
    <p class="front-email">kwcoatingsjobs@mailbox.com</p>
  </section>

  <section class="card card--striped">
    <div class="stripe-row stripe-row--top">
      <span class="chip chip--pale"></span><span class="gap"></span>
      <span class="chip chip--mid"></span><span class="gap gap--wide"></span>
      <span class="chip chip--royal"></span><span class="gap gap--end"></span>
      <span class="chip chip--navy"></span>
    </div>
    <div class="brand">
      <div class="brand__line"><span class="brand__mark"></span><span class="brand__name">KW Coatings</span></div>
      <span class="brand__site">kwcoatings.com.au</span>
    </div>
    <p class="front-email">kwcoatingsjobs@mailbox.com</p>
    <div class="stripe-row stripe-row--bottom">
      <span class="chip chip--pale"></span><span class="gap"></span>
      <span class="chip chip--mid"></span><span class="gap gap--wide"></span>
      <span class="chip chip--royal"></span><span class="gap gap--end"></span>
      <span class="chip chip--navy"></span>
    </div>
  </section>

  <section class="card card--kevin">
    <div class="swatch-face">
      <div class="brand">
        <div class="brand__line"><span class="brand__mark"></span><span class="brand__name">KW Coatings</span></div>
        <span class="brand__site">kwcoatings.com.au</span>
      </div>
      <div class="band band--navy"></div>
      <p class="line line--name">Kevin Walsh</p>
      <div class="band band--royal"></div>
      <p class="line line--phone">0400 182 736</p>
      <div class="band band--mid"></div>
      <p class="line line--service">Commercial &amp; Domestic Painting</p>
      <div class="band band--pale"></div>
      <p class="line line--contact"><span>Contact us</span><span>kwcoatingsjobs@mailbox.com</span></p>
    </div>
  </section>

  <section class="card card--leon">
    <div class="swatch-face">
      <div class="brand">
        <div class="brand__line"><span class="brand__mark"></span><span class="brand__name">KW Coatings</span></div>
        <span class="brand__site">kwcoatings.com.au</span>
      </div>
      <div class="band band--navy"></div>
      <p class="line line--name">Leon Harper</p>
      <div class="band band--royal"></div>
      <p class="line line--phone">0455 06 290 317</p>
      <div class="band band--mid"></div>
      <p class="line line--service">Commercial &amp; Domestic Painting</p>
      <div class="band band--pale"></div>
      <p class="line line--contact"><span>Contact us</span><span>kwcoatingsjobs@mailbox.com</span></p>
    </div>
  </section>

</main>
</body>
</html>
```